New Stationary and Logo Design for Start Up Company

We need a logo design and stationary set including letterhead, business card (double sided), compliments slip and envelope for a new company Bright Quill Media.
The files should be editable to update address and standard contact details, will need to forward to web designer and stationary printer.
The company will be an online marketer and distributer of various business education products in Australia.
The designs should convey simple clean image
Target Market(s)
Small business owners and professional service providers (ie Accountants, Lawyers, Real Estate Agents) in Australia
Industry/Entity Type
Education
Look and feel
Each slider illustrates characteristics of the customer's brand and the style your logo design should communicate.

```html
<!DOCTYPE html>
<html lang="en">
<head>
<meta charset="utf-8">
<title>Bright Quill Media – Stationery Set</title>
<link rel="stylesheet" href="https://fonts.googleapis.com/css2?family=Lexend:wght@400&family=Archivo:ital,wght@1,800&family=Dancing+Script:wght@500&display=swap">
<style>
  :root {
    --olive: #b4aa00;
    --olive-dark: #a29800;
    --olive-soft: #d7d07a;
    --ink: #111111;
    --paper: #ffffff;
    --brand-font: "Lexend", sans-serif;
    --label-font: "Archivo", sans-serif;
    --script-font: "Dancing Script", cursive;
  }
  * { box-sizing: border-box; margin: 0; padding: 0; }
  html, body { width: 1200px; height: 734px; overflow: hidden; background: var(--paper); }
  .canvas { position: relative; width: 1200px; height: 734px; font-family: var(--brand-font); color: var(--ink); }
  .piece { position: absolute; overflow: hidden; background: var(--paper); }
  .brand-name { font-family: var(--brand-font); font-weight: 400; color: var(--ink); white-space: nowrap; letter-spacing: -0.02em; }
  .brand-dot { display: inline-block; border-radius: 50%; background: var(--olive); vertical-align: middle; }
  .label { position: absolute; font-family: var(--label-font); font-style: italic; font-weight: 800; font-size: 12px; color: var(--ink); white-space: nowrap; }
  .tagline { font-family: var(--script-font); color: var(--olive-soft); font-size: 12px; }

  /* Letterhead */
  .letterhead { left: 0; top: 0; width: 483px; height: 705px; border: 1px solid var(--olive); }
  .letterhead__band { position: absolute; left: 0; top: 0; }
  .letterhead__brand { position: absolute; left: 16px; top: 50px; font-size: 14px; }
  .letterhead__brand .brand-dot { width: 8px; height: 8px; margin-right: 5px; }
  .letterhead__address { position: absolute; left: 257px; top: 38px; color: var(--paper); font-size: 9px; }
  .letterhead__footer { position: absolute; left: 0; bottom: 0; width: 100%; height: 26px; background: var(--olive); text-align: center; line-height: 26px; }

  /* Compliments slip */
  .slip { left: 494px; top: 0; width: 545px; height: 270px; border: 1px solid var(--olive); }
  .slip__curve { position: absolute; left: 0; bottom: 0; }
  .slip__brand { position: absolute; left: 14px; top: 42px; font-size: 18px; }
  .slip__brand .brand-dot { width: 10px; height: 10px; margin-right: 6px; }
  .slip__address { position: absolute; left: 149px; top: 108px; width: 285px; height: 44px; border: 1px solid var(--olive); border-radius: 12px; font-size: 9px; text-align: center; line-height: 42px; }

  /* Primary logo */
  .logo-lockup { position: absolute; left: 546px; top: 412px; font-size: 46px; line-height: 1; }
  .logo-lockup .brand-dot { width: 18px; height: 18px; margin-right: 12px; }

  /* Business cards */
  .card-front { left: 508px; top: 477px; width: 258px; height: 138px; border: 1px solid var(--olive); }
  .card-front__swoosh { position: absolute; right: 0; top: 0; }
  .card-front__brand { position: absolute; left: 0; width: 100%; top: 50px; text-align: center; font-size: 16px; }
  .card-front__name { position: absolute; left: 0; width: 100%; top: 80px; text-align: center; font-size: 9px; }
  .card-front__phone { position: absolute; left: 0; width: 100%; top: 92px; text-align: center; font-size: 13px; font-weight: 400; color: var(--olive); letter-spacing: 0.04em; }
  .card-front__tagline { position: absolute; left: 0; width: 100%; top: 108px; text-align: center; font-size: 8px; color: var(--olive); }

  .card-back { left: 784px; top: 476px; width: 263px; height: 141px; background: var(--olive-dark); }
  .card-back__mark { position: absolute; left: 76px; top: 8px; width: 110px; height: 60px; border-radius: 6px; background: linear-gradient(180deg, rgba(255,255,255,0.18), rgba(255,255,255,0.04)); }
  .card-back__panel { position: absolute; left: 20px; top: 75px; width: 223px; height: 34px; border: 1px solid var(--olive-soft); border-radius: 7px; text-align: center; color: var(--paper); padding-top: 3px; }
  .card-back__headline { font-size: 8.5px; font-weight: 400; letter-spacing: 0.03em; }
  .card-back__detail { font-size: 7px; line-height: 1.15; }
  .card-back__tagline { position: absolute; left: 0; width: 100%; top: 116px; text-align: center; }

  /* Email signature */
  .email-signature { position: absolute; left: 622px; top: 646px; }
  .email-signature__brand { position: absolute; left: 655px; top: 679px; font-size: 11px; }
</style>
</head>
<body>
<main class="canvas">

  <!-- Letterhead -->
  <section class="piece letterhead">
    <svg class="letterhead__band" width="483" height="75" viewBox="0 0 483 75" aria-hidden="true">
      <polygon points="121,0 483,0 483,74 208,74" fill="var(--olive)"/>
      <polygon points="121,0 150,0 212,74 208,74" fill="var(--olive-dark)"/>
    </svg>
    <div class="letterhead__brand brand-name"><span class="brand-dot"></span>Bright Quill Media</div>
    <p class="letterhead__address">Your company address here</p>
    <div class="letterhead__footer"><span class="tagline">Improve Your Future</span></div>
  </section>
  <p class="label" style="left:176px; top:715px;">letterhead</p>

  <!-- Compliments slip & envelope -->
  <section class="piece slip">
    <svg class="slip__curve" width="545" height="60" viewBox="0 0 545 60" aria-hidden="true">
      <path d="M0,0 C10,35 60,50 140,52 L545,52 L545,60 L0,60 Z" fill="var(--olive)"/>
    </svg>
    <div class="slip__brand brand-name"><span class="brand-dot"></span>Bright Quill Media</div>
    <p class="slip__address">Your company address here</p>
    <p class="label" style="left:263px; top:230px;">Compliments slip &amp; Envelope</p>
  </section>

  <!-- Logo design -->
  <div class="logo-lockup brand-name"><span class="brand-dot"></span>Bright Quill Media</div>
  <p class="label" style="left:920px; top:456px;">logo design</p>

  <!-- Business card front -->
  <section class="piece card-front">
    <svg class="card-front__swoosh" width="60" height="24" viewBox="0 0 60 24" aria-hidden="true">
      <path d="M0,0 L60,0 L60,24 C50,10 30,4 0,0 Z" fill="var(--olive)"/>
    </svg>
    <div class="card-front__brand brand-name"><span class="brand-dot" style="width:7px;height:7px;margin-right:4px;"></span>Bright Quill Media</div>
    <p class="card-front__name">Daniel Harte</p>
    <p class="card-front__phone">0398765412</p>
    <p class="card-front__tagline tagline">Improve Your Future</p>
  </section>
  <p class="label" style="left:516px; top:623px;">Front Businesses card</p>

  <!-- Business card back -->
  <section class="piece card-back">
    <div class="card-back__mark" role="img" aria-label="Faint brand emblem area"></div>
    <div class="card-back__panel">
      <p class="card-back__headline">we are online company provides</p>
      <p class="card-back__detail">accounting / tax education packages<br>for small businesses</p>
    </div>
    <p class="card-back__tagline tagline">Improve Your Future</p>
  </section>
  <p class="label" style="left:811px; top:622px;">Right Businesses card</p>

  <!-- Email signature -->
  <svg class="email-signature" width="160" height="78" viewBox="0 0 160 78" aria-hidden="true">
    <ellipse cx="80" cy="39" rx="78" ry="37" fill="var(--paper)" stroke="var(--olive)" stroke-width="2"/>
    <path d="M60,3 C110,0 155,15 158,39 C150,25 115,10 60,3 Z" fill="var(--olive)"/>
  </svg>
  <div class="email-signature__brand brand-name">Bright Quill Media</div>
  <p class="label" style="left:830px; top:686px;">email signature</p>

</main>
</body>
</html>
```